Transform Your Giving

I need a tri-fold brochure that will fit in a standard number 10 business envelope. Harborline and Steadfast Services is a charitable nonprofit. The goal of this brochure is to stimulate people into thinking about other ways to make a donation. The design should communicate the essential information on donation options, create a sense of professional integrity, be graphically sharp, easy to read and laid out in a way that doesn't make the material appear crowded.

```html
<!DOCTYPE html>
<html lang="en">
<head>
<meta charset="utf-8">
<title>Transform Your Giving – Tri-fold Brochure</title>
<link href="https://fonts.googleapis.com/css2?family=Montserrat:ital,wght@0,300;0,400;0,500;0,600;0,700;0,800;1,400&display=swap" rel="stylesheet">
<style>
:root{
  --navy:#2b2a6e;
  --navy-deep:#24235f;
  --green:#4cb748;
  --bg:#c6bebb;
  --panel:#ebebeb;
  --panel-light:#f6f6f6;
  --ink:#3a3a48;
  --white:#fff;
}
*{margin:0;padding:0;box-sizing:border-box}
html,body{width:1200px;height:1200px;overflow:hidden}
body{background:var(--bg);font-family:'Montserrat',sans-serif;color:var(--ink);position:relative}
.spread{position:absolute;left:274px;width:663px;height:516px;overflow:hidden}
.spread-front{top:71px;background:var(--white)}
.spread-inside{top:621px;background:var(--panel)}
.backdrop{position:absolute;inset:0;width:663px;height:516px}
.abs{position:absolute}
.center{text-align:center}

/* front – left panel */
.impact-title{left:0;width:217px;top:19px;font-weight:800;font-size:16.5px;line-height:19px;color:var(--navy);text-align:center}
.impact-title span{color:var(--green);display:block}
.impact-copy{left:22px;width:174px;top:65px;font-size:8.2px;line-height:9.9px;font-weight:400;text-align:center;color:var(--ink)}
.option-list{left:45px;top:156px;width:132px;list-style:none}
.option-list li{height:16px;border:1px solid var(--green);margin-bottom:5.2px;display:flex;align-items:center;justify-content:center;gap:4px;font-size:8.6px;color:var(--ink)}
.option-list svg{width:8px;height:8px}

/* front – middle panel */
.brand{width:110px;text-align:center;font-weight:800;font-size:10px;line-height:11px;color:var(--navy)}
.brand::before{content:"";display:block;width:9px;height:9px;border-radius:50%;background:var(--green);margin:0 auto 3px}
.brand-mid{left:280px;top:14px}
.brand-right{left:438px;top:14px}
.learn-copy{left:248px;width:172px;top:71px;font-size:8.3px;line-height:10.1px;font-weight:500;text-align:center;color:var(--ink)}
.quote{left:252px;width:166px;top:251px;font-style:italic;font-size:8.6px;line-height:10.5px;color:#d9d9ee;text-align:center}
.quote cite{display:block;font-style:normal;color:var(--green);font-weight:500;font-size:7.6px;margin-top:2px}
.will{left:225px;width:220px;top:298px;text-align:center;color:var(--white);font-size:8px;line-height:10.5px}
.will .will-url{display:block;color:var(--green);font-weight:800;font-size:12.6px;line-height:16px}
.will .will-free{font-weight:700;font-size:8.8px}
.contact-btn{left:281px;top:359px;width:97px;height:17px;border-radius:9px;background:var(--green);color:var(--white);font-weight:800;font-size:10.5px;display:flex;align-items:center;justify-content:center}
.more{left:225px;width:220px;top:382px;text-align:center;color:var(--white);font-size:8px;line-height:10px}
.more strong{display:block;font-size:11px;font-weight:800;line-height:13px}
.rule{height:1px;background:rgba(255,255,255,.55)}
.rule-mid{left:234px;width:193px;top:421px}
.contacts{top:430px;font-size:6px;line-height:8px;color:var(--white);font-weight:500}
.contacts svg{position:absolute;left:-9px;width:6px;height:6px}
.contacts-addr{left:251px}
.contacts-tel{left:339px}
.follow{left:290px;top:460px;font-size:7.8px;color:var(--white);display:flex;align-items:center;gap:3px}
.follow i{display:inline-block;width:8px;height:8px;border-radius:50%;background:var(--green)}
.disclaimer{left:240px;width:190px;top:479px;font-size:3.7px;line-height:4.6px;color:#cfcfe6;text-align:center}

/* front – right panel */
.transform{left:434px;width:229px;top:393px;text-align:center;font-weight:800;color:var(--white);font-size:17.5px;line-height:20px}
.transform span{display:block;color:var(--green);font-size:24.5px;line-height:27px}
.rule-right{left:451px;width:193px;background:rgba(255,255,255,.7)}
.mantra{left:434px;width:229px;top:449px;display:flex;justify-content:center;gap:6px;color:var(--white);font-weight:800;font-size:10.6px}
.mantra span{display:flex;align-items:center;gap:3px}
.mantra svg{width:11px;height:11px}
.discover{left:434px;width:229px;top:476px;text-align:center;color:var(--white);font-weight:700;font-size:7.2px;line-height:9.6px}

/* inside */
.ways-badge{left:18px;top:19px;width:188px;height:66px;border-radius:33px;background:var(--navy);border:2px solid var(--white);box-shadow:0 0 0 1px #d8d8e6;display:flex;align-items:center;padding-left:18px;gap:4px}
.ways-badge .ways-num{font-weight:800;font-size:58px;line-height:58px;color:var(--green)}
.ways-badge .ways-text{font-weight:800;font-size:15px;line-height:15.5px;color:var(--white)}
.badge-tip{left:62px;top:84px;width:0;height:0;border-left:7px solid transparent;border-right:7px solid transparent;border-top:7px solid var(--navy)}
.way-title{font-weight:700;font-size:12.3px;line-height:14.7px;color:var(--navy)}
.way-lede{font-weight:700;font-size:6.9px;line-height:8.8px;color:var(--green)}
.way-copy{font-size:6.9px;line-height:8.85px;font-weight:400;color:var(--ink)}
.how{height:13.5px;padding:0 7px;border-radius:4px;background:var(--green);color:var(--white);font-size:7.4px;font-weight:500;display:inline-flex;align-items:center}
.tick-item{padding-left:15px}
.tick-item svg{position:absolute;left:0;top:1px;width:10px;height:10px}
</style>
</head>
<body>

<!-- ============ FRONT (outside) ============ -->
<section class="spread spread-front" aria-label="Brochure outside spread">
  <svg class="backdrop" viewBox="0 0 663 516">
    <defs>
      <linearGradient id="photoCouple" x1="0" y1="0" x2="1" y2="1">
        <stop offset="0" stop-color="#f3b44a"/>
        <stop offset=".45" stop-color="#9a6a3a"/>
        <stop offset="1" stop-color="#6a7a3c"/>
      </linearGradient>
      <linearGradient id="photoMan" x1="0" y1="0" x2="1" y2="0">
        <stop offset="0" stop-color="#ffffff"/>
        <stop offset=".35" stop-color="#dfe4da"/>
        <stop offset=".7" stop-color="#b56a4c"/>
        <stop offset="1" stop-color="#4f6a3a"/>
      </linearGradient>
      <polygon id="hx" points="0,-33 28.6,-16.5 28.6,16.5 0,33 -28.6,16.5 -28.6,-16.5"/>
    </defs>

    <path d="M217,99 Q250,190 330,205 Q430,250 540,222 Q640,190 663,40 L663,516 L217,516 Z" fill="var(--navy)"/>
    <path role="img" aria-label="Photo: smiling older man in a rust shirt holding a mug on a porch" d="M405,0 L663,0 L663,40 Q625,200 455,222 Q405,215 395,180 Z" fill="url(#photoMan)"/>
    <path d="M331,180 Q430,265 560,225 Q640,190 656,40" fill="none" stroke="var(--green)" stroke-width="9" stroke-linecap="round"/>

    <path d="M0,270 Q150,262 236,400 L236,516 L0,516 Z" fill="var(--green)"/>
    <path role="img" aria-label="Photo: older couple smiling while reading a map outdoors at sunset" d="M0,284 Q140,282 222,405 L222,516 L0,516 Z" fill="url(#photoCouple)"/>

    <use href="#hx" x="331" y="225" transform="translate(331 225) scale(.62) translate(-331 -225)" fill="var(--green)"/>
    <text x="331" y="240" text-anchor="middle" fill="#fff" font-family="Montserrat,sans-serif" font-weight="800" font-size="30">“</text>

    <g fill="var(--green)">
      <use href="#hx" x="478" y="292"/>
      <use href="#hx" x="546" y="292"/>
      <use href="#hx" x="614" y="292"/>
      <use href="#hx" x="512" y="348"/>
      <use href="#hx" x="580" y="348"/>
    </g>
    <g fill="none" stroke="#fff" stroke-width="1.3">
      <circle cx="478" cy="286" r="11"/><circle cx="478" cy="286" r="7.5"/>
      <path d="M538,294 h16 M539,291 h14 M540,291 v-8 M544,291 v-8 M548,291 v-8 M552,291 v-8 M538,282 l8,-6 l8,6 z"/>
      <path d="M606,294 h16 M607,293 v-6 h3 v6 M612,293 v-9 h3 v9 M617,293 v-12 h3 v12 M606,284 l5,-4 l4,2 l6,-6"/>
      <path d="M504,350 h16 M505,349 v-6 h3 v6 M510,349 v-9 h3 v9 M515,349 v-12 h3 v12 M504,340 l5,-4 l4,2 l6,-6"/>
      <path d="M572,350 h16 M573,349 v-6 h3 v6 M578,349 v-9 h3 v9 M583,349 v-12 h3 v12 M572,340 l5,-4 l4,2 l6,-6"/>
    </g>
    <g fill="#fff" font-family="Montserrat,sans-serif" font-weight="700" font-size="5.2" text-anchor="middle">
      <text x="478" y="306">Crypto</text>
      <text x="546" y="306">DAF’s</text>
      <text x="614" y="303">Stocks &amp;</text><text x="614" y="310">Securities</text>
      <text x="512" y="359">Stocks &amp;</text><text x="512" y="366">Securities</text>
      <text x="580" y="359">Stocks &amp;</text><text x="580" y="366">Securities</text>
    </g>
  </svg>

  <h1 class="abs impact-title">THE IMPACT OF <span>YOUR GIFT</span></h1>
  <p class="abs impact-copy">Your generosity drives our mission. With every Smart gift you’re supporting Harborline and Steadfast Services. Join our community of Smart Givers today and make an enduring impact.&nbsp; With Smart Giving your generosity reaches further.&nbsp; Begin your Smart Giving journey with us today.</p>
  <ul class="abs option-list">
    <li><svg viewBox="0 0 10 10"><circle cx="5" cy="5" r="4.2" fill="none" stroke="#4cb748"/><path d="M3,5 l1.5,1.5 l2.7,-3" fill="none" stroke="#4cb748"/></svg>Stocks and Securities</li>
    <li><svg viewBox="0 0 10 10"><circle cx="5" cy="5" r="4.2" fill="none" stroke="#4cb748"/><path d="M3,5 l1.5,1.5 l2.7,-3" fill="none" stroke="#4cb748"/></svg>DAFs</li>
    <li><svg viewBox="0 0 10 10"><circle cx="5" cy="5" r="4.2" fill="none" stroke="#4cb748"/><path d="M3,5 l1.5,1.5 l2.7,-3" fill="none" stroke="#4cb748"/></svg>QCDs</li>
    <li><svg viewBox="0 0 10 10"><circle cx="5" cy="5" r="4.2" fill="none" stroke="#4cb748"/><path d="M3,5 l1.5,1.5 l2.7,-3" fill="none" stroke="#4cb748"/></svg>Crypto</li>
    <li><svg viewBox="0 0 10 10"><circle cx="5" cy="5" r="4.2" fill="none" stroke="#4cb748"/><path d="M3,5 l1.5,1.5 l2.7,-3" fill="none" stroke="#4cb748"/></svg>Charitable Annuity</li>
  </ul>

  <div class="abs brand brand-mid">Harborline &amp; Steadfast</div>
  <p class="abs learn-copy">To learn more about Smart Giving Options and how they can benefit you and Harborline and Steadfast Services, please reach out to our team.&nbsp; We’re here to help you navigate these giving methods and answer any question you may have.</p>
  <blockquote class="abs quote">Being kind to others is a way of being good to yourself.<cite>Miriam Halvorsen</cite></blockquote>
  <p class="abs will">If you do not have a will<span class="will-url">go to www.Easywillkit.com</span>In 20 minutes you can have a<br><span class="will-free">legal will – for free.</span></p>
  <div class="abs contact-btn">CONTACT US</div>
  <p class="abs more"><strong>Have more question?</strong>Please contact us at Harborline and<br>Steadfast Services</p>
  <div class="abs rule rule-mid"></div>
  <p class="abs contacts contacts-addr"><svg viewBox="0 0 6 6" style="top:1px"><circle cx="3" cy="2.5" r="2" fill="none" stroke="#4cb748" stroke-width=".8"/><path d="M3,4.5 v1.5" stroke="#4cb748" stroke-width=".8"/></svg>1420 Meadowbrook Ave.<br>Suite 9<br>Fairview, ND&nbsp; 58000</p>
  <p class="abs contacts contacts-tel"><svg viewBox="0 0 6 6" style="top:1px"><rect x="1.5" y=".5" width="3" height="5" rx=".6" fill="none" stroke="#4cb748" stroke-width=".7"/></svg>555-014-2200 (ext. 100)<br>info@harborlinesteadfast.org<br>www.harborlinesteadfast.org</p>
  <p class="abs follow">Follow us <i></i></p>
  <p class="abs disclaimer">This material is provided for general information only and is not intended as tax, accounting or legal advice. Harborline and Steadfast Services is not a financial adviser. Please speak with your own tax or financial professional before making any decision about Smart Giving.</p>

  <div class="abs brand brand-right">Harborline &amp; Steadfast</div>
  <h2 class="abs transform">TRANSFORM <span>YOUR GIVING</span></h2>
  <div class="abs rule rule-right" style="top:444px"></div>
  <p class="abs mantra">
    <span><svg viewBox="0 0 12 12"><circle cx="6" cy="6" r="5" fill="none" stroke="#4cb748" stroke-width="1.2"/><path d="M3.5,6 l2,2 l3.5,-4" fill="none" stroke="#4cb748" stroke-width="1.2"/></svg>Be Strategic</span>
    <span><svg viewBox="0 0 12 12"><circle cx="6" cy="6" r="5" fill="none" stroke="#4cb748" stroke-width="1.2"/><path d="M3.5,6 l2,2 l3.5,-4" fill="none" stroke="#4cb748" stroke-width="1.2"/></svg>Be Smart</span>
  </p>
  <div class="abs rule rule-right" style="top:466px"></div>
  <p class="abs discover">Discover the impact of Smart Giving with<br>Harborline and Steadfast Services</p>
</section>

<!-- ============ INSIDE ============ -->
<section class="spread spread-inside" aria-label="Brochure inside spread">
  <svg class="backdrop" viewBox="0 0 663 516">
    <defs>
      <linearGradient id="photoDrive" x1="0" y1="0" x2="1" y2="1">
        <stop offset="0" stop-color="#7d9b5e"/>
        <stop offset=".5" stop-color="#9fb7a6"/>
        <stop offset=".8" stop-color="#3f78b8"/>
        <stop offset="1" stop-color="#2f4f8a"/>
      </linearGradient>
      <polygon id="hxi" points="0,-31 26.8,-15.5 26.8,15.5 0,31 -26.8,15.5 -26.8,-15.5"/>
    </defs>
    <rect x="217" y="0" width="221" height="516" fill="var(--panel-light)"/>
    <path d="M165,78 Q300,170 470,118 Q565,85 605,0 L590,0 Q470,132 260,112 Q200,105 165,78 Z" fill="var(--green)"/>
    <path role="img" aria-label="Photo: smiling older man driving a blue convertible beside a river" d="M110,0 L590,0 Q470,132 260,112 Q190,104 140,60 Z" fill="url(#photoDrive)"/>
    <path d="M170,516 Q300,430 470,470 Q320,450 195,516 Z" fill="var(--green)"/>
    <path d="M195,516 Q330,452 475,516 Z" fill="var(--navy)"/>

    <g fill="var(--navy)">
      <use href="#hxi" x="45" y="135"/>
      <use href="#hxi" x="45" y="337"/>
      <use href="#hxi" x="268" y="186"/>
      <use href="#hxi" x="478" y="91"/>
      <use href="#hxi" x="484" y="338"/>
    </g>
    <g fill="none" stroke="#fff" stroke-width="1.2">
      <path d="M33,147 h24 M35,146 v-8 h4 v8 M42,146 v-12 h4 v12 M49,146 v-16 h4 v16 M34,132 l6,-5 l6,3 l8,-8"/>
      <path d="M33,350 h24 M35,347 h20 M37,346 v-11 M41,346 v-11 M45,346 v-11 M49,346 v-11 M53,346 v-11 M34,333 h22 l-11,-8 z"/>
      <circle cx="268" cy="186" r="15"/><circle cx="268" cy="186" r="10.5"/>
      <path d="M265,180 v12 M265,180 h4 q3,0 3,3 q0,3 -3,3 h-4 M265,186 h5 q3,0 3,3 q0,3 -3,3 h-5"/>
      <path d="M467,92 h20 v14 h-20 z M465,86 h24 v6 h-24 z M477,86 v20 M477,86 q-6,-8 -9,-3 q0,4 9,3 q6,-8 9,-3 q0,4 -9,3"/>
      <circle cx="482" cy="338" r="11"/><path d="M482,327 v-3 M479,324 h6 M482,338 l5,-5"/>
      <circle cx="492" cy="347" r="5"/>
    </g>
  </svg>

  <div class="abs ways-badge"><span class="ways-num">5</span><span class="ways-text">STRATEGIC<br>AND SMART<br>WAYS</span></div>
  <div class="abs badge-tip"></div>

  <!-- left column -->
  <h3 class="abs way-title" style="left:82px;top:111px;width:130px">Gifts of Stocks or Appreciated Assets Strategic &amp; Smart</h3>
  <p class="abs way-lede" style="left:82px;top:157px;width:125px">Consider your long-term publicly traded stock as a way to give to your favorite charity.</p>
  <p class="abs way-copy" style="left:18px;top:186px;width:190px">You can make a significantly bigger impact when you donate long-term appreciated securities, including stock, mutual funds, and bonds, directly to your favorite charity.</p>
  <span class="abs how" style="left:18px;top:224px">How Does It Work?</span>
  <p class="abs way-copy" style="left:18px;top:249px;width:193px">When you donate stock to a charity, you will generally take a tax deduction for the full market value.&nbsp; Because you are donating stock, your contribution and tax deduction may be significantly higher than contributing the after-tax proceeds.&nbsp; The same benefits apply when you donate mutual funds or bonds.</p>

  <h3 class="abs way-title" style="left:82px;top:314px;width:120px">Donor-Advised Fund (DAF) Strategic &amp; Smart</h3>
  <p class="abs way-lede" style="left:81px;top:359px;width:130px">Consider a DAF – a simple, flexible, and tax-advantageous way to give to your favorite charities.</p>
  <p class="abs way-copy" style="left:18px;top:390px;width:190px">A Donor-Advised Fund (DAF), is like a charitable investment account for the sole purpose of supporting your favorite charities.</p>
  <span class="abs how" style="left:18px;top:417px">How Does It Work?</span>
  <p class="abs way-copy" style="left:18px;top:442px;width:195px">You establish a DAF and contribute cash, stocks, or non-publicly traded assets, cryptocurrency, and private company stock to be eligible for an immediate tax deduction.&nbsp; Those funds are contributed for tax-free growth.&nbsp; You can recommend grants be made from your DAF to any IRS qualified public charity.</p>

  <!-- middle column -->
  <h3 class="abs way-title" style="left:306px;top:165px;width:130px">Cryptocurrency Strategic &amp; Smart</h3>
  <p class="abs way-lede" style="left:306px;top:196px;width:125px">Consider donating Bitcoin and other cryptocurrencies to your favorite charity.</p>
  <p class="abs way-copy" style="left:240px;top:230px;width:190px">Bitcoin and other cryptocurrencies can be donated to charity just like other appreciated assets such as stocks and other business interests.&nbsp; Before you sell bitcoin and donate the after-tax proceeds, consider donating your bitcoin directly to a favorite charity.</p>
  <span class="abs how" style="left:240px;top:279px">How Does It Work?</span>
  <p class="abs way-copy" style="left:240px;top:306px;width:185px">Many donors find it useful to open a Donor-Advised Fund (DAF).&nbsp; This strategy includes two significant benefits, both for you and your favorite charity.</p>
  <p class="abs way-copy tick-item" style="left:240px;top:340px;width:190px"><svg viewBox="0 0 10 10"><circle cx="5" cy="5" r="4.2" fill="none" stroke="#4cb748"/><path d="M3,5 l1.5,1.5 l2.7,-3" fill="none" stroke="#4cb748"/></svg>Your tax deduction will be equal to the fair market value of the donated bitcoin (as determined by a qualified appraisal).</p>
  <p class="abs way-copy tick-item" style="left:240px;top:375px;width:190px"><svg viewBox="0 0 10 10"><circle cx="5" cy="5" r="4.2" fill="none" stroke="#4cb748"/><path d="M3,5 l1.5,1.5 l2.7,-3" fill="none" stroke="#4cb748"/></svg>Your cryptocurrency donation is tax-smart because it may eliminate capital gains taxes on the value / appreciation AND your favorite charity will receive 100% of the value of the contribution.</p>
  <p class="abs way-copy" style="left:240px;top:422px;width:185px">Often charities are not able to accept direct donations of bitcoin/crypto so using a DAF is a great way to donate these assets.</p>

  <!-- right column -->
  <h3 class="abs way-title" style="left:519px;top:66px;width:135px">Qualified Charitable Distributions (QCDs) Strategic &amp; Smart</h3>
  <p class="abs way-lede" style="left:519px;top:112px;width:130px">Consider a QCD – when planning your IRA withdrawal strategy…and donate to your favorite charity.</p>
  <p class="abs way-copy" style="left:452px;top:144px;width:195px">IRA owners at age 70 ½ or over can transfer dollars from their IRA to charity tax-free each year. These transfers known as Qualified Charitable Distributions (QCDs) offer eligible older Americans a great way to easily give to charity.</p>
  <span class="abs how" style="left:452px;top:193px">How Does It Work?</span>
  <p class="abs way-copy" style="left:452px;top:220px;width:205px">Are you 72 and required to take a minimum distribution (RMD) from your IRA but do not need the funds?&nbsp; Consider a Qualified Charitable Distribution. Normally, distributions from a traditional IRA are taxable when received.&nbsp; With a QCD, these distributions become tax-free when paid directly from the IRA to your favorite eligible charity.&nbsp; An IRA owner wishing to make a QCD should contact their IRA trustee, allowing time to complete the transaction before the end of the year to receive the tax benefit.</p>

  <h3 class="abs way-title" style="left:524px;top:311px;width:130px">Charitable Gift Annuity Strategic &amp; Smart</h3>
  <p class="abs way-lede" style="left:524px;top:355px;width:130px">Consider establishing a Charitable Gift Annuity</p>
  <p class="abs way-copy" style="left:452px;top:379px;width:195px">You make a donation to a single charity. The gift is set aside in a reserve account and invested.</p>
  <span class="abs how" style="left:452px;top:400px">How Does It Work?</span>
  <p class="abs way-copy" style="left:452px;top:425px;width:205px">A charitable gift annuity is a contract between a donor and a charity.&nbsp; As a donor, you make a sizable gift to charity using cash, securities, or possibly other assets. This money is then invested.&nbsp; In return, you become eligible to take a partial tax deduction for your donation, plus you receive a fixed stream of income from the charity for the rest of your life.&nbsp; At the end of your life (as well as your spouse’s, if you’re giving as a couple), the charity receives the remainder of the gift.</p>
</section>

</body>
</html>
```